Modernise Business Card

Our company has been operating for 10 years. With the start of the new decade we are looking to refresh our business card design. We manufacture a range of industrial product shipping to customers internationally. A copy of our current card, both sides, is attached. We are looking for a mature professional appearance.

```html
<!DOCTYPE html>
<html lang="en">
<head>
<meta charset="utf-8">
<title>Vantrel Business Card</title>
<link rel="stylesheet" href="https://fonts.googleapis.com/css2?family=Lato:wght@400;900&family=Roboto:wght@400;500&family=Ubuntu+Condensed&display=swap">
<style>
  :root {
    --backdrop: #d9d3c9;
    --card-core: #3a3a3f;
    --card-edge: #000000;
    --accent: #29aee6;
    --accent-deep: #1f93c4;
    --steel: #b9bcc0;
    --text-light: #d2d2d2;
    --text-contact: #d9d9d9;
  }
  * { margin: 0; padding: 0; box-sizing: border-box; }
  html, body { width: 1200px; height: 1200px; overflow: hidden; }
  body { background: var(--backdrop); position: relative; }
  .card {
    position: absolute;
    left: 191px;
    width: 816px;
    height: 498px;
    background: radial-gradient(ellipse 60% 75% at 52% 52%, var(--card-core) 0%, #1c1c1f 55%, var(--card-edge) 100%);
    overflow: hidden;
  }
  .card--front { top: 78px; }
  .card--back { top: 625px; }
  .card svg { position: absolute; inset: 0; width: 816px; height: 498px; }
  .holder-name { font-family: "Ubuntu Condensed", sans-serif; font-size: 57px; fill: var(--text-light); }
  .contact-line { font-family: "Lato", sans-serif; font-size: 16.5px; fill: var(--text-contact); }
  .brand-name { font-family: "Lato", sans-serif; font-weight: 900; fill: var(--accent); }
  .service-line { font-family: "Roboto", sans-serif; font-weight: 500; font-size: 19px; fill: var(--text-light); }
  .site-link { font-family: "Roboto", sans-serif; font-size: 17px; letter-spacing: 0.8px; fill: var(--accent); }
  .icon { fill: var(--accent); }
  .icon-stroke { fill: none; stroke: var(--accent); stroke-width: 1.6; }
</style>
</head>
<body>

<section class="card card--front" aria-label="Business card front">
  <svg viewBox="0 0 816 498" xmlns="http://www.w3.org/2000/svg">
    <defs>
      <linearGradient id="band-blue" x1="0" y1="0" x2="1" y2="0">
        <stop offset="0" stop-color="var(--accent-deep)"/>
        <stop offset="1" stop-color="#3fa6c9"/>
      </linearGradient>
      <linearGradient id="band-blue-r" x1="1" y1="0" x2="0" y2="0">
        <stop offset="0" stop-color="var(--accent-deep)"/>
        <stop offset="1" stop-color="#3fa6c9"/>
      </linearGradient>
    </defs>
    <g class="corner-band corner-band--top-left">
      <polygon points="0,0 67,0 67,198 0,242" fill="var(--steel)"/>
      <polygon points="0,0 56,0 56,192 0,226" fill="url(#band-blue)"/>
    </g>
    <g class="corner-band corner-band--bottom-right">
      <polygon points="748,301 816,257 816,498 748,498" fill="var(--steel)"/>
      <polygon points="759,306 816,273 816,498 759,498" fill="url(#band-blue-r)"/>
    </g>

    <text class="holder-name" x="115" y="169">Owen Barrick</text>

    <g class="contact-icons">
      <path class="icon" d="M404,206 c4,-3 8,-2 9,1 l4,10 c1,3 -1,5 -3,6 l-3,2 c2,6 7,12 13,15 l3,-2 c2,-2 5,-2 7,0 l7,6 c2,2 2,5 0,7 c-3,3 -7,5 -12,4 c-14,-3 -27,-17 -29,-33 c-1,-7 1,-13 4,-16 z"/>
      <rect x="410" y="262" width="27" height="17" fill="var(--accent)"/>
      <polyline points="410,263 423.5,273 437,263" fill="none" stroke="#111" stroke-width="1.6"/>
      <polyline points="410,279 420,271 M437,279 427,271" fill="none" stroke="#111" stroke-width="1.2"/>
      <g class="icon-globe">
        <circle class="icon-stroke" cx="423" cy="302" r="11.5"/>
        <ellipse class="icon-stroke" cx="423" cy="302" rx="5" ry="11.5"/>
        <line class="icon-stroke" x1="411.5" y1="302" x2="434.5" y2="302"/>
        <line class="icon-stroke" x1="413" y1="296" x2="433" y2="296"/>
        <line class="icon-stroke" x1="413" y1="308" x2="433" y2="308"/>
        <polygon class="icon" points="428,303 438,313 434,313 437,319 435,320 432,314 429,317"/>
      </g>
      <g class="icon-pin">
        <path class="icon" d="M419,327 c-6,0 -11,5 -11,11 c0,8 11,19 11,19 c0,0 11,-11 11,-19 c0,-6 -5,-11 -11,-11 z"/>
        <circle cx="419" cy="338" r="4" fill="#1a1a1c"/>
        <ellipse cx="419" cy="359" rx="7" ry="2.5" fill="var(--accent)"/>
      </g>
    </g>

    <g class="contact-lines">
      <text class="contact-line" x="449" y="220">China:&#160; +86 150 2267 0419</text>
      <text class="contact-line" x="449" y="243">Australia: +61 412 385 707</text>
      <text class="contact-line" x="449" y="276">obarrick@vantrelfittings.com</text>
      <text class="contact-line" x="449" y="309">www.vantrelfittings.com</text>
      <text class="contact-line" x="449" y="345">808-3, Lian Feng Building</text>
      <text class="contact-line" x="449" y="365">41 Qiaoxi Road, Haishu District</text>
      <text class="contact-line" x="704" y="385" text-anchor="end">Ningbo 315010 China</text>
    </g>

    <text class="brand-name" x="47" y="425" font-size="54">Vantrel</text>
  </svg>
</section>

<section class="card card--back" aria-label="Business card back">
  <svg viewBox="0 0 816 498" xmlns="http://www.w3.org/2000/svg">
    <defs>
      <linearGradient id="band-blue-b" x1="0" y1="0" x2="1" y2="0">
        <stop offset="0" stop-color="var(--accent-deep)"/>
        <stop offset="1" stop-color="#3fa6c9"/>
      </linearGradient>
      <linearGradient id="band-blue-br" x1="1" y1="0" x2="0" y2="0">
        <stop offset="0" stop-color="var(--accent-deep)"/>
        <stop offset="1" stop-color="#3fa6c9"/>
      </linearGradient>
    </defs>
    <g class="corner-band corner-band--bottom-left">
      <polygon points="0,256 68,300 68,498 0,498" fill="var(--steel)"/>
      <polygon points="0,272 57,306 57,498 0,498" fill="url(#band-blue-b)"/>
    </g>
    <g class="corner-band corner-band--top-right">
      <polygon points="748,0 816,0 816,241 748,197" fill="var(--steel)"/>
      <polygon points="759,0 816,0 816,227 759,193" fill="url(#band-blue-br)"/>
    </g>

    <text class="brand-name" x="403" y="283" font-size="118" text-anchor="middle">Vantrel</text>

    <g class="service-list">
      <text class="service-line" x="91" y="402">HYDRAULIC ADAPTERS</text>
      <text class="service-line" x="91" y="430">HOUSE FITTINGS</text>
      <text class="service-line" x="91" y="457">QUICK COUPLING</text>
    </g>

    <text class="site-link" x="787" y="453" text-anchor="end">www.vantrelfittings.com</text>
  </svg>
</section>

</body>
</html>
```